job vacancy cover page

I need to design a one pager for a job I'd like to apply for. The one I have done looks shit and amateur!! Wanting it to look amazing and professional (Not too professional though as they are pretty young and fun).

```html
<!DOCTYPE html>
<html lang="en">
<head>
<meta charset="utf-8">
<title>Why me? – Cover page</title>
<link href="https://fonts.googleapis.com/css2?family=Montserrat:wght@400;500;600;700&display=swap" rel="stylesheet">
<style>
:root{
  --paper:#efefef;
  --teal:#1f8f99;
  --teal-dark:#1c7f88;
  --line:#21838f;
  --ink:#1b1b1b;
  --green:#2fb24a;
  --blue:#0a7fe0;
  --orange:#f7931e;
  --indigo:#2b1f78;
  --yellow:#ffd200;
  --white:#ffffff;
}
*{margin:0;padding:0;box-sizing:border-box}
html,body{width:1200px;height:774px;overflow:hidden}
body{font-family:"Montserrat",sans-serif;background:var(--paper);color:var(--ink);position:relative}
.page{position:absolute;inset:0;background:linear-gradient(125deg,#ececec 0%,#f7f7f7 30%,#ececec 48%,#f6f6f6 70%,#ececec 100%)}
.title-box{position:absolute;left:496px;top:61px;width:208px;height:56px;border:2px solid var(--line);border-radius:16px;display:flex;align-items:center;justify-content:center;font-weight:600;font-size:37px;color:var(--line)}
.connectors{position:absolute;left:0;top:0}
.hero-art{position:absolute;left:122px;top:110px;width:148px;height:62px;border-radius:32px;background:linear-gradient(90deg,#f0a35e,#c9443d 45%,#3a9fd0)}
.card{position:absolute;top:215px;width:282px;height:182px;border:3px solid;border-radius:14px;background:var(--white);overflow:hidden}
.card-head{height:34px;display:flex;align-items:center;justify-content:center;color:var(--white);font-weight:700;font-size:14px;letter-spacing:.2px}
.card-body{padding:10px 10px 0 14px;font-size:13px;line-height:1.3}
.card--green .card-body{padding-left:20px}
.card--green{left:98px;border-color:var(--green)}
.card--green .card-head{background:var(--green)}
.card--blue{left:461px;border-color:var(--blue)}
.card--blue .card-head{background:var(--blue)}
.card--orange{left:824px;border-color:var(--orange)}
.card--orange .card-head{background:var(--orange)}
.powers-intro{font-size:15px;margin-bottom:2px}
.powers{list-style:none;font-weight:600;font-size:15.5px;line-height:1.3}
.powers li::before,.small-list li::before{content:"• "}
.small-list{list-style:none}
.small-list li{padding-left:9px;text-indent:-9px;margin-bottom:4px;font-size:11.8px;line-height:1.25}
.card--blue .small-list li:nth-child(2){padding-right:46px}
.trophy-art{position:absolute;left:238px;top:68px;width:34px;height:48px;border-radius:12px 12px 5px 5px;background:linear-gradient(180deg,#f6c21a,#e08a12)}
.band{position:absolute;left:0;top:457px;width:1200px;height:317px;background:linear-gradient(180deg,var(--teal),var(--teal-dark));border-top:3px solid var(--indigo)}
.band-title{position:absolute;left:467px;top:432px;width:267px;height:49px;border-radius:9px;background:var(--indigo);color:var(--white);font-weight:600;font-size:25px;display:flex;align-items:center;justify-content:center}
.col{position:absolute;top:523px;color:var(--white)}
.col h2{color:var(--yellow);font-weight:600;font-size:27px;padding-bottom:6px;display:inline-block;border-bottom:2px solid var(--yellow)}
.col ul{list-style:none;margin-top:8px;font-size:18.5px;line-height:1.2}
.col li{padding-left:16px;text-indent:-16px;margin-bottom:7px}
.col li::before{content:"• "}
.col--values{left:34px}
.col--offer{left:481px}
.col--projects{left:808px}
.col--projects ul{font-size:17px}
.col--projects li{margin-bottom:11px}
.col--projects strong{font-weight:600;font-size:19px}
</style>
</head>
<body>
<div class="page">
  <div class="title-box">Why me?</div>

  <svg class="connectors" width="1200" height="215" viewBox="0 0 1200 215" fill="none" stroke="var(--line)" stroke-width="2">
    <path d="M585 128 V160 a11 11 0 0 1 -11 11 H248 a11 11 0 0 0 -11 11 V212"/>
    <path d="M600 128 V212"/>
    <path d="M616 128 V160 a11 11 0 0 0 11 11 H952 a11 11 0 0 1 11 11 V212"/>
    <g fill="var(--line)" stroke="none">
      <circle cx="585" cy="128" r="3.5"/><circle cx="600" cy="128" r="3.5"/><circle cx="616" cy="128" r="3.5"/>
      <circle cx="237" cy="212" r="3.5"/><circle cx="600" cy="212" r="3.5"/><circle cx="963" cy="212" r="3.5"/>
    </g>
  </svg>

  <div class="hero-art" role="img" aria-label="Illustration of a caped superhero flying"></div>

  <section class="card card--green">
    <div class="card-head">IF I WAS A SUPERHERO</div>
    <div class="card-body">
      <p class="powers-intro">My four superpowers would be:</p>
      <ul class="powers">
        <li>Proactiveness</li>
        <li>Creativity</li>
        <li>Pride in my work</li>
        <li>Organisational skills</li>
      </ul>
    </div>
  </section>

  <section class="card card--blue">
    <div class="card-head">SOME OF MY SUCCESS</div>
    <div class="card-body">
      <ul class="small-list">
        <li>Increased client workshops by 85%<br>across accounts.</li>
        <li>Delivered double digit revenue increase.</li>
        <li>Re-designed workshops for virtual<br>delivery, maintaining key relationships.</li>
      </ul>
    </div>
    <div class="trophy-art" role="img" aria-label="Illustration of a gold trophy"></div>
  </section>

  <section class="card card--orange">
    <div class="card-head">PASSION</div>
    <div class="card-body">
      <ul class="small-list">
        <li>The development of others and / or<br>their teams.</li>
        <li>Helping people learn and be successful<br>in life and in their careers.</li>
        <li>Exceptional client experiences</li>
      </ul>
    </div>
  </section>

  <div class="band" role="img" aria-label="Teal-tinted photo of a team meeting around a table"></div>
  <div class="band-title">Why Brightfield?</div>

  <section class="col col--values">
    <h2>Values that Stood out</h2>
    <ul>
      <li>Change for the better</li>
      <li>Excellence – not mediocre</li>
      <li>Put your heart into it and<br>give a shit</li>
      <li>Going the extra mile</li>
      <li>Take risks</li>
    </ul>
  </section>

  <section class="col col--offer">
    <h2>What you offer</h2>
    <ul>
      <li>Learning &amp; Developing</li>
      <li>Team</li>
      <li>Flexibility</li>
      <li>Fun</li>
    </ul>
  </section>

  <section class="col col--projects">
    <h2>Interesting projects</h2>
    <ul>
      <li><strong>Cordana -</strong> Leadership development<br>and team effectiveness</li>
      <li><strong>Halvern –</strong> Change management<br>for true transformation</li>
      <li><strong>Ashby's –</strong> Customer centricity at Australia's<br>most iconic department store</li>
    </ul>
  </section>
</div>
</body>
</html>
```